Vemboraa Silver Gifts needs an attractive PRODUCT catalog

We need a catalog for our products. We are manufacturers of fine sterling silver gifts. We sell baby gifts, mens gifts, entertaining gifts, etc. We need a simple, elegant and attractive catalog for our retailers to view our entire collection of products.
We need a simple yet impressive product catalog for our company. We sell silver gifts of all kinds and need to design a catalog with images, prices and information on our products to give our clients and sales rep. The primary purpose of the catalog is to showcase our products clearly. However we require a high end looking catalog to represent our product line. We have about 100- 150 products. We don't need something fancy where our product line is not clearly showcased. But a design factor to the catalog is what we are looking for.

We have our brand colors and logo.

Industry/Entity Type

Gift Shop

Font styles to use
Serif

Colors
ec1f27
ffffff
aaaaaa

Requirements
Must have
• An Introduction page
• A reference of categories by pages
• A photo, SKU, Price for each product
Nice to have
• A hint of our brand colors in a subtle way
Should not have
• Too much color

```html
<!DOCTYPE html>
<html lang="en">
<head>
<meta charset="utf-8">
<title>Vemboraa Silver Gifts – Product Catalog 2016 - 2017</title>
<link rel="stylesheet" href="https://fonts.googleapis.com/css2?family=Open+Sans:wght@400;600&display=swap">
<style>
  :root {
    --backdrop: #e9e7e3;
    --page-top: #f2f2f2;
    --page-bottom: #e1e1e2;
    --title: #5a5a5a;
    --year: #d65a2e;
    --tile-dark: #9e9ea1;
    --tile-mid: #b2b2b4;
    --tile-light: #bfbfc2;
    --photo-white: #fbfbfb;
    --silver-light: #e8e8ea;
    --silver-mid: #c6c6c9;
    --silver-deep: #a9a9ad;
    --blush: #e7b9cf;
    --brand-red: #ec1f27;
    --brand-ink: #1e1e1e;
    --url: #9a9a9a;
  }
  * { box-sizing: border-box; margin: 0; padding: 0; }
  html, body { width: 1200px; height: 804px; overflow: hidden; }
  body {
    background: var(--backdrop);
    font-family: "Open Sans", Arial, sans-serif;
    position: relative;
  }
  .cover {
    position: absolute;
    left: 340px; top: 32px;
    width: 520px; height: 740px;
    background: linear-gradient(160deg, var(--page-top), var(--page-bottom));
    box-shadow: 0 6px 18px rgba(0,0,0,0.18);
  }
  .cover-title {
    position: absolute; top: 104px; left: 0; width: 100%;
    text-align: center;
    font-size: 30px; font-weight: 400; color: var(--title);
    letter-spacing: 0.3px;
  }
  .cover-years {
    position: absolute; top: 166px; left: 0; width: 100%;
    text-align: center;
    font-size: 14px; color: var(--year); letter-spacing: 0.5px;
  }
  .product-grid {
    position: absolute; top: 222px; left: 64px;
    display: grid;
    grid-template-columns: repeat(3, 128px);
    grid-template-rows: repeat(3, 128px);
    gap: 4px;
  }
  .tile { width: 128px; height: 128px; }
  .tile--photo { background-color: var(--photo-white); }
  .tile--napkin-ring {
    background: linear-gradient(135deg, var(--photo-white) 18%, var(--silver-light) 36%, var(--silver-deep) 50%, var(--silver-light) 62%, var(--photo-white) 82%);
  }
  .tile--frame {
    background: linear-gradient(160deg, var(--photo-white) 15%, var(--silver-mid) 38%, var(--blush) 55%, var(--silver-mid) 70%, var(--photo-white) 88%);
  }
  .tile--cufflinks {
    background: linear-gradient(120deg, var(--photo-white) 20%, var(--silver-mid) 40%, var(--silver-light) 50%, var(--silver-deep) 60%, var(--photo-white) 82%);
  }
  .tile--cup {
    background: linear-gradient(90deg, var(--photo-white) 14%, var(--silver-light) 30%, var(--silver-mid) 50%, var(--silver-light) 70%, var(--photo-white) 88%);
  }
  .tile--rattle {
    background: linear-gradient(150deg, var(--photo-white) 22%, var(--silver-light) 40%, var(--silver-deep) 54%, var(--silver-light) 66%, var(--photo-white) 84%);
  }
  .tile--infinity {
    background: linear-gradient(110deg, var(--photo-white) 16%, var(--silver-mid) 36%, var(--photo-white) 50%, var(--silver-mid) 64%, var(--photo-white) 86%);
  }
  .tile--dark { background: var(--tile-dark); }
  .tile--mid { background: var(--tile-mid); }
  .tile--light { background: var(--tile-light); }
  .brand-mark {
    position: absolute; top: 640px; left: 50%;
    transform: translateX(-50%);
    display: flex; align-items: center; gap: 10px;
    background: #ffffff;
    padding: 10px 22px;
  }
  .brand-mark__dot { width: 10px; height: 10px; background: var(--brand-red); }
  .brand-mark__name {
    font-size: 28px; font-weight: 400; color: var(--brand-ink);
    letter-spacing: 3px;
  }
  .cover-url {
    position: absolute; top: 708px; left: 0; width: 100%;
    text-align: center;
    font-size: 11px; color: var(--url); letter-spacing: 2.5px;
  }
</style>
</head>
<body>
  <main class="cover">
    <h1 class="cover-title">Product Catalog</h1>
    <p class="cover-years">2016 - 2017</p>

    <section class="product-grid">
      <div class="tile tile--photo tile--napkin-ring" role="img" aria-label="Polished silver napkin ring"></div>
      <div class="tile tile--photo tile--frame" role="img" aria-label="Silver teddy bear photo frame with pink insert"></div>
      <div class="tile tile--dark"></div>
      <div class="tile tile--mid"></div>
      <div class="tile tile--photo tile--cufflinks" role="img" aria-label="Pair of square silver cufflinks"></div>
      <div class="tile tile--photo tile--cup" role="img" aria-label="Silver baby cup with handle"></div>
      <div class="tile tile--photo tile--rattle" role="img" aria-label="Silver moon and star baby rattle ring"></div>
      <div class="tile tile--photo tile--infinity" role="img" aria-label="Silver infinity cufflinks"></div>
      <div class="tile tile--light"></div>
    </section>

    <div class="brand-mark">
      <span class="brand-mark__dot"></span>
      <span class="brand-mark__name">vemboraa</span>
    </div>
    <p class="cover-url">www.vemboraa.com</p>
  </main>
</body>
</html>
```